Business is called "Pelton Ledger". Accounting and tax services.

I need a flyer for my new business "Pelton Ledger". I am an individual accountant working for himself on the Sunshine Coast in Queensland Australia. I would like to see designs that communicate reliability and trust. I believe my point of difference is that I am always available to my clients and I will cap my number of clients to ensure I can service them properly. Accountants in general seem to have a bad reputation for not responding to clients in a timely fashion, whether by email or phone. This is where I intend to differentiate myself. I have included my business card for ideas on colour and for contact information. I have also included some logo's that should go on the flyer. With the QLA logo, the words "Pelton Ledger is a QLA Business" needs to be written either above, below or to the right hand side (as per the business card).

Target Market(s)

Small business owners and individuals requiring taxation and financials

Industry/Entity Type

Public Accounting

Font styles to use
Serif

Requirements
Must have
• Supplied logo's, accounting style pictures etc
Services: Small Business Taxation
Company & Trust Tax Returns
Rental Property Returns
Capital Gains Tax
Individual Tax Returns
BAS and IAS lodgements
Nice to have
• Needs to convey a sense of being reliable and responds to clients quickly.
Should not have
• My name

```html
<!DOCTYPE html>
<html lang="en">
<head>
<meta charset="utf-8">
<title>Pelton Ledger – Flyer</title>
<link rel="stylesheet" href="https://fonts.googleapis.com/css2?family=Oswald:wght@400;500;600&family=Lato:wght@400;700&display=swap">
<style>
  :root {
    --stage: #25314b;
    --navy: #1f2a44;
    --teal: #51b3c7;
    --teal-deep: #4aa9bd;
    --sky: #5bc2d6;
    --paper: #ffffff;
    --ink: #1b2338;
    --photo-light: #eef0f1;
    --photo-mid: #b9bcc0;
    --photo-dark: #3a3d44;
  }
  * { margin: 0; padding: 0; box-sizing: border-box; }
  html, body { width: 1200px; height: 1083px; overflow: hidden; background: var(--stage); }
  .canvas { position: relative; width: 1200px; height: 1083px; }
  .flyer-frame {
    position: absolute; left: 231px; top: 20px;
    width: 737px; height: 1043px; overflow: hidden;
  }
  .flyer {
    position: absolute; left: 0; top: 0;
    width: 1130px; height: 1600px;
    background: var(--paper);
    transform: scale(0.6522); transform-origin: top left;
    font-family: 'Lato', sans-serif; color: var(--ink);
  }
  .flyer-shapes { position: absolute; inset: 0; }

  .brand { position: absolute; left: 600px; top: 24px; width: 330px; text-align: center; }
  .brand-mark { display: block; margin: 0 auto 14px; width: 78px; height: 78px; border: 3px solid var(--ink); border-radius: 50%; }
  .brand-name { display: block; font-size: 26px; letter-spacing: 9px; line-height: 1; color: var(--ink); }

  .headline { position: absolute; left: 96px; top: 236px; color: var(--paper); font-family: 'Oswald', sans-serif; font-weight: 400; }
  .headline-name { display: block; font-size: 106px; font-weight: 600; line-height: 1.1; letter-spacing: -1px; }
  .headline-tag { display: block; font-size: 60px; font-weight: 400; line-height: 1.1; margin-top: 6px; }

  .intro { position: absolute; left: 100px; top: 555px; width: 440px; font-size: 30px; line-height: 37px; color: var(--ink); }
  .intro strong { font-weight: 700; }

  .phone { position: absolute; left: 104px; top: 745px; display: flex; align-items: center; gap: 26px; }
  .phone-icon { width: 62px; height: 80px; }
  .phone-number { font-family: 'Oswald', sans-serif; font-size: 64px; font-weight: 500; line-height: 1; color: var(--paper); }

  .services-title { position: absolute; left: 95px; top: 972px; font-family: 'Oswald', sans-serif; font-size: 82px; font-weight: 500; line-height: 1.1; color: var(--teal-deep); }
  .services-list { position: absolute; list-style: none; width: 420px; }
  .services-list.col-left { left: 60px; top: 1108px; }
  .services-list.col-right { left: 617px; top: 1108px; }
  .services-list li { position: relative; padding-left: 40px; font-size: 29px; line-height: 32px; height: 66px; }
  .services-list li.two-line { line-height: 27px; margin-top: -6px; height: 72px; }
  .services-list li::before { content: ""; position: absolute; left: 0; top: 9px; width: 17px; height: 17px; background: var(--teal); }
  .services-list li.two-line::before { top: 20px; }

  .contact { position: absolute; left: 54px; top: 1460px; }
  .contact-row { display: flex; align-items: center; gap: 16px; height: 50px; font-family: 'Oswald', sans-serif; font-size: 40px; color: var(--sky); }
  .contact-icon { width: 30px; height: 30px; }

  .partner, .institute {
    position: absolute; top: 1418px; display: flex; align-items: center; gap: 14px;
    font-size: 40px; font-weight: 700; line-height: 1; color: var(--navy);
  }
  .partner { left: 640px; }
  .institute { left: 850px; }
  .partner-dot { width: 22px; height: 22px; background: var(--teal); }
  .institute-block { width: 64px; height: 64px; background: var(--navy); }
</style>
</head>
<body>
<main class="canvas">
  <div class="flyer-frame">
    <article class="flyer">
      <svg class="flyer-shapes" viewBox="0 0 1130 1600" width="1130" height="1600" aria-hidden="true">
        <defs>
          <linearGradient id="photo-tone" x1="0" y1="0" x2="1" y2="1">
            <stop offset="0" stop-color="var(--photo-dark)"/>
            <stop offset="0.35" stop-color="var(--photo-mid)"/>
            <stop offset="0.6" stop-color="var(--photo-light)"/>
            <stop offset="1" stop-color="#f7f7f7"/>
          </linearGradient>
        </defs>
        <polygon class="header-panel" points="35,225 352,30 772,250 960,150 1060,225 1060,600 35,522" fill="var(--navy)"/>
        <polygon class="intro-band" points="38,522 590,510 760,980 560,1067 38,838" fill="var(--teal)"/>
        <polyline class="top-chevron" points="345,0 772,240 1140,24" fill="none" stroke="var(--sky)" stroke-width="14"/>
        <polygon class="top-chevron-fill" points="360,0 772,232 1130,22 1130,0" fill="var(--paper)"/>
        <polygon class="photo-frame" points="955,190 578,415 583,875 960,1100 1340,875 1340,415" fill="var(--sky)"/>
        <polygon class="photo-area" role="img" aria-label="Photo of a calculator with stacks of copper coins" points="955,212 596,425 600,865 960,1080 1330,865 1330,425" fill="url(#photo-tone)"/>
        <polyline class="footer-chevron" points="0,1435 232,1298 620,1524 620,1600" fill="none" stroke="var(--sky)" stroke-width="16"/>
        <polygon class="footer-panel" points="0,1455 232,1320 604,1536 604,1600 0,1600" fill="var(--navy)"/>
      </svg>

      <header class="brand">
        <span class="brand-mark"></span>
        <span class="brand-name">PELTON LEDGER</span>
      </header>

      <h1 class="headline">
        <span class="headline-name">Pelton Ledger</span>
        <span class="headline-tag">is a QLA Business"</span>
      </h1>

      <p class="intro">I am an individual accountant working for himself on the Sunshine <strong>Coast in Queensland Australia</strong></p>

      <div class="phone">
        <svg class="phone-icon" viewBox="0 0 68 80">
          <path d="M14 4 L24 2 L30 20 L22 26 C24 38 30 48 40 56 L48 50 L62 62 L56 72 C40 80 10 52 6 24 C5 14 8 8 14 4 Z" fill="var(--ink)"/>
          <path d="M44 10 A14 14 0 0 1 58 24 M44 18 A7 7 0 0 1 51 25" fill="none" stroke="var(--ink)" stroke-width="3"/>
        </svg>
        <span class="phone-number">0412 586 903</span>
      </div>

      <h2 class="services-title">Services</h2>
      <ul class="services-list col-left">
        <li>Small Business Taxation</li>
        <li class="two-line">Company &amp; Trust Tax<br>Returns</li>
        <li>Rental Property Returns</li>
      </ul>
      <ul class="services-list col-right">
        <li>Capital Gains Tax</li>
        <li>Individual Tax Returns</li>
        <li>BAS and IAS lodgements</li>
      </ul>

      <footer class="contact">
        <div class="contact-row">
          <svg class="contact-icon" viewBox="0 0 30 30"><rect x="2" y="7" width="26" height="17" fill="none" stroke="var(--paper)" stroke-width="2"/><polyline points="2,7 15,17 28,7" fill="none" stroke="var(--paper)" stroke-width="2"/></svg>
          <span>hello@peltonledger.com.au</span>
        </div>
        <div class="contact-row">
          <svg class="contact-icon" viewBox="0 0 30 30"><circle cx="15" cy="15" r="12" fill="none" stroke="var(--paper)" stroke-width="2"/><ellipse cx="15" cy="15" rx="5" ry="12" fill="none" stroke="var(--paper)" stroke-width="2"/><line x1="3" y1="15" x2="27" y2="15" stroke="var(--paper)" stroke-width="2"/></svg>
          <span>www.peltonledger.com.au</span>
        </div>
      </footer>

      <div class="partner"><span class="partner-dot"></span>Tallyo</div>
      <div class="institute"><span class="institute-block"></span>QLA</div>
    </article>
  </div>
</main>
</body>
</html>
```